Visual Print Advert for Hair & Makeup Artist

One page colour visual advertisement required for a hair and makeup artist business using pictures and logo with brief description and contact details. MUST have plain white background. All information will be provided I just need someone to put it in a good layout.
Professional, clean and appealing to the eye. Don't want it to look over crowded or busy.
Layout should feature 2-7 photos, without making the page look too busy. Can use any of the photos provided and you are welcome to crop them to change the orientation of the photo.
Content and typeface should fit in with logo and be modern but appeal to the female target audience of brides in Australia aged 22-40yo.
Advertisement is be be used in a bridal magazine and other print media for business advertising purposes.
Updates

Target Market(s)

Future brides in Australia aged 22 - 40yo - females only

Industry/Entity Type

Business

Colors
e34197
ffffff
eda3c7

Requirements
Must have
• White background
Should not have
• NO script writing as it doesn't fit with the logo.

```html
<!DOCTYPE html>
<html lang="en">
<head>
<meta charset="utf-8">
<title>Avelle Makeup Artistry – Bridal Advert</title>
<link href="https://fonts.googleapis.com/css2?family=Jost:wght@300;400&display=swap" rel="stylesheet">
<style>
  :root {
    --brand-pink: #e34197;
    --bright-pink: #f25bc6;
    --soft-pink: #eda3c7;
    --paper: #f8f8f8;
    --ink: #222222;
    --stage: #ece9ee;
    --charcoal: #2b2b2b;
  }
  html, body {
    margin: 0;
    padding: 0;
    width: 1041px;
    height: 1200px;
    overflow: hidden;
    background: var(--stage);
    font-family: "Jost", "Futura", sans-serif;
  }
  .advert {
    position: absolute;
    left: 91px;
    top: 0;
    width: 774px;
    height: 1081px;
    background: var(--paper);
    transform: scale(1.1101);
    transform-origin: top left;
    overflow: hidden;
    color: var(--ink);
  }
  .advert-art {
    position: absolute;
    inset: 0;
    width: 774px;
    height: 1081px;
  }
  .brand {
    position: absolute;
    left: 62px;
    top: 48px;
    width: 372px;
    text-align: right;
  }
  .brand-name {
    display: block;
    font-weight: 300;
    font-size: 62px;
    letter-spacing: 12px;
    line-height: 1;
    color: var(--charcoal);
    text-align: left;
  }
  .brand-tagline {
    display: block;
    margin-top: 4px;
    font-weight: 400;
    font-size: 13px;
    letter-spacing: 3px;
    color: #555;
  }
  .intro {
    position: absolute;
    left: 63px;
    top: 158px;
    margin: 0;
    font-weight: 400;
    font-size: 25px;
    line-height: 34px;
    color: var(--ink);
  }
  .social-list {
    position: absolute;
    left: 45px;
    top: 881px;
    display: flex;
    gap: 12px;
    margin: 0;
    padding: 0;
    list-style: none;
  }
  .social-list li {
    width: 34px;
    height: 34px;
    border-radius: 50%;
    background: var(--bright-pink);
  }
  .contact-list {
    position: absolute;
    left: 44px;
    top: 936px;
    margin: 0;
    padding: 0;
    list-style: none;
  }
  .contact-list li {
    display: flex;
    align-items: center;
    height: 37px;
    font-size: 22px;
    color: var(--ink);
  }
  .contact-list svg {
    width: 22px;
    height: 22px;
    margin-right: 17px;
    flex: none;
  }
  .specialty {
    position: absolute;
    right: 68px;
    top: 863px;
    margin: 0;
    font-size: 20px;
    line-height: 28px;
    text-align: right;
    color: var(--ink);
  }
</style>
</head>
<body>
<main class="advert">
  <svg class="advert-art" viewBox="0 0 774 1081" xmlns="http://www.w3.org/2000/svg">
    <defs>
      <linearGradient id="garden" x1="0" y1="0" x2="0.3" y2="1">
        <stop offset="0" stop-color="#24461c"/>
        <stop offset="0.45" stop-color="#4f7a35"/>
        <stop offset="0.75" stop-color="#8aa46a"/>
        <stop offset="1" stop-color="#e9e4d8"/>
      </linearGradient>
      <linearGradient id="ribbon" x1="0" y1="0" x2="1" y2="1">
        <stop offset="0" stop-color="#f7b6dd" stop-opacity="0.15"/>
        <stop offset="0.5" stop-color="#f58fd0" stop-opacity="0.9"/>
        <stop offset="1" stop-color="#f7b6dd" stop-opacity="0.2"/>
      </linearGradient>
      <radialGradient id="party" cx="0.5" cy="0.45" r="0.6">
        <stop offset="0" stop-color="#c9b3a4"/>
        <stop offset="1" stop-color="#4a4a4e"/>
      </radialGradient>
      <radialGradient id="portrait" cx="0.5" cy="0.45" r="0.6">
        <stop offset="0" stop-color="#e7cfc4"/>
        <stop offset="1" stop-color="#6b5550"/>
      </radialGradient>
      <radialGradient id="updo" cx="0.5" cy="0.5" r="0.6">
        <stop offset="0" stop-color="#d9c2b0"/>
        <stop offset="1" stop-color="#8c9a68"/>
      </radialGradient>
    </defs>

    <!-- soft ribbon sweeping down the left -->
    <path d="M40,400 C20,560 140,760 300,880 C360,930 420,1000 440,1081 L415,1081 C390,1010 330,950 270,900 C110,770 10,600 40,400 Z" fill="url(#ribbon)"/>

    <!-- garden bride feature photo -->
    <path d="M520,0 L774,0 L774,1081 L455,1081 C500,1000 505,930 465,870 C420,720 300,520 330,410 C365,300 560,210 545,95 C540,55 532,25 520,0 Z"
          fill="url(#garden)" role="img" aria-label="Photo of a bride in a lace gown with a floral crown, standing in a leafy garden"/>

    <!-- pink wave framing the photo -->
    <path d="M450,0 C500,30 525,60 520,100 C505,200 360,290 320,400" fill="none" stroke="var(--bright-pink)" stroke-width="0"/>
    <path d="M462,0 L520,0 C532,25 540,55 545,95 C560,210 365,300 330,410 L318,405 C350,300 530,200 522,100 C518,55 495,25 462,0 Z" fill="var(--bright-pink)"/>
    <path d="M465,870 C505,930 500,1000 455,1081 L478,1081 C520,1000 525,930 480,860 Z" fill="var(--bright-pink)"/>
    <!-- charcoal sweep at the base -->
    <path d="M372,1081 C430,1020 470,960 460,880 L474,872 C500,960 480,1030 455,1081 Z" fill="var(--charcoal)"/>

    <!-- circular photo trio -->
    <circle cx="219" cy="460" r="127" fill="url(#party)" stroke="var(--bright-pink)" stroke-width="6"
            role="img" aria-label="Photo of a smiling bride with her three bridesmaids"/>
    <circle cx="256" cy="696" r="110" fill="url(#portrait)" stroke="var(--bright-pink)" stroke-width="6"
            role="img" aria-label="Close-up bridal makeup portrait with veil"/>
    <circle cx="373" cy="828" r="91" fill="url(#updo)" stroke="var(--bright-pink)" stroke-width="6"
            role="img" aria-label="Photo of a bride's braided updo hairstyle outdoors"/>
  </svg>

  <header class="brand">
    <span class="brand-name">AVELLE</span>
    <span class="brand-tagline">MAKEUP ARTISTRY</span>
  </header>

  <p class="intro">Professionally trained<br>and certified mobile Hair &amp;<br>Makeup Artists with<br>over 10 years experience</p>

  <ul class="social-list" aria-label="Social media">
    <li></li><li></li><li></li><li></li>
  </ul>

  <ul class="contact-list">
    <li>
      <svg viewBox="0 0 24 24" aria-hidden="true"><circle cx="12" cy="12" r="10.5" fill="none" stroke="var(--bright-pink)" stroke-width="1.5"/><path d="M8.5,6.5 l2,2.2 -1.2,1.6 c0.8,1.8 2,3 3.8,3.8 l1.6,-1.2 2.2,2 -1.4,1.8 c-4,-0.4 -8,-4.4 -8.4,-8.4 z" fill="var(--bright-pink)"/></svg>
      0412 345 678
    </li>
    <li>
      <svg viewBox="0 0 24 24" aria-hidden="true"><rect x="3" y="6" width="18" height="12" fill="none" stroke="var(--bright-pink)" stroke-width="1.5"/><path d="M3,6 L12,13 L21,6" fill="none" stroke="var(--bright-pink)" stroke-width="1.5"/></svg>
      hello@avellemakeup.com.au
    </li>
    <li>
      <svg viewBox="0 0 24 24" aria-hidden="true"><circle cx="12" cy="12" r="9.5" fill="none" stroke="var(--bright-pink)" stroke-width="1.5"/><ellipse cx="12" cy="12" rx="4" ry="9.5" fill="none" stroke="var(--bright-pink)" stroke-width="1.5"/><path d="M2.5,12 H21.5" stroke="var(--bright-pink)" stroke-width="1.5"/></svg>
      www.avellemakeup.com.au
    </li>
  </ul>

  <p class="specialty">We Specialize<br>in naturally<br>enhancing your<br>beauty to have you<br>looking and feeling<br>your best on your<br>special day.</p>
</main>
</body>
</html>
```